Banner Design 4040mm W x 2190mm H

Design a glamorous and exciting 4040mm W x 2190mm H backdrop for the QMRTE Velvet Orchid Gala at the luxurious Marlow Hall, Tessel, Wexley Quay, Sydney. This exciting backdrop should be spectacular so that people will be excited to take photos in front of it.
Design Colours preferred is black and pink.
Please include our website on the banner www.qmrte.org.au
Should include the words "QMRTE Velvet Orchid Gala" as the main attraction on the banner.
Please include "Thank you to our sponsors" and include the logo of the sponsors.
Sponsors:
Brindle Pathology
Kestrel Radiology
JNX Diagnostic Imaging
Harwick Legal Group
Dunmores
Banner Template:
4040mm W x 2190mm H Single Sided (.AI)
https://files.qorvashare.example/f/7TzKp2mWq9LxR4nB/view
QMRTE Logo:
Can be obtained from our website www.qmrte.org.au

```html
<!DOCTYPE html>
<html lang="en">
<head>
<meta charset="utf-8">
<title>QMRTE Velvet Orchid Gala – Backdrop</title>
<link rel="stylesheet" href="https://fonts.googleapis.com/css2?family=Montserrat:wght@500;600;700;800&family=Kaushan+Script&family=Roboto+Condensed:wght@400&display=swap">
<style>
  :root {
    --page: #efefef;
    --paper: #ffffff;
    --ink: #111111;
    --black-band: #0b0b0c;
    --pink: #dd137b;
    --pink-soft: #e4549a;
    --grey-text: #6b6b6b;
    --rule: #c9c9c9;
    --sponsor-ink: #4a4a4a;
  }
  * { margin: 0; padding: 0; box-sizing: border-box; }
  html, body {
    width: 1200px;
    height: 995px;
    overflow: hidden;
    background: var(--page);
  }
  .backdrop {
    position: absolute;
    left: 30px;
    top: 188px;
    width: 1140px;
    height: 618px;
    background: var(--paper);
    overflow: hidden;
    box-shadow: 0 2px 10px rgba(0,0,0,0.12);
  }
  .backdrop-shapes {
    position: absolute;
    inset: 0;
    width: 1140px;
    height: 618px;
  }
  .sparkle-field, .staff-figures {
    position: absolute;
  }
  .sparkle-field--top-left {
    left: 0; top: 0; width: 320px; height: 350px;
    background: radial-gradient(ellipse at 30% 30%, rgba(221,19,123,0.16), rgba(221,19,123,0) 70%);
  }
  .sparkle-field--bottom-right {
    left: 1020px; top: 325px; width: 110px; height: 230px;
    background: radial-gradient(ellipse at 50% 50%, rgba(221,19,123,0.14), rgba(221,19,123,0) 70%);
  }
  .staff-figures {
    left: 818px; top: 43px; width: 262px; height: 225px;
    background: linear-gradient(180deg, rgba(200,200,200,0.18), rgba(200,200,200,0.05));
    border-radius: 40px 40px 0 0;
  }
  .client-mark {
    position: absolute;
    left: 178px; top: 140px;
    width: 150px;
    display: flex; align-items: center; gap: 8px;
    font-family: "Montserrat", sans-serif;
    font-weight: 700;
    font-size: 24px;
    color: var(--ink);
  }
  .client-mark__dot {
    width: 18px; height: 18px; border-radius: 50%;
    background: var(--pink);
  }
  .event-title {
    position: absolute;
    left: 385px; top: 84px;
  }
  .event-title__org {
    display: block;
    font-family: "Montserrat", sans-serif;
    font-weight: 800;
    font-size: 66px;
    line-height: 1;
    letter-spacing: 1px;
    color: var(--ink);
  }
  .event-title__name {
    display: block;
    margin-top: 8px;
    font-family: "Kaushan Script", cursive;
    font-size: 66px;
    line-height: 1.1;
    color: var(--pink);
    white-space: nowrap;
  }
  .sponsor-heading {
    position: absolute;
    left: 0; width: 1140px; top: 322px;
    text-align: center;
    font-family: "Montserrat", sans-serif;
    font-size: 15px;
    font-weight: 600;
    color: var(--grey-text);
  }
  .sponsor-heading__small { font-size: 10px; font-weight: 500; }
  .sponsor-heading__accent { color: var(--pink); font-weight: 700; letter-spacing: 0.5px; }
  .sponsor-list {
    position: absolute;
    left: 164px; width: 804px; top: 372px;
    display: flex;
    justify-content: space-between;
    align-items: center;
    list-style: none;
  }
  .sponsor {
    width: 150px;
    text-align: center;
    font-family: "Montserrat", sans-serif;
    font-weight: 600;
    font-size: 12px;
    color: var(--sponsor-ink);
    display: flex; justify-content: center; align-items: center; gap: 6px;
  }
  .sponsor__square {
    width: 12px; height: 12px; background: var(--sponsor-ink);
  }
  .venue {
    position: absolute;
    left: 67px; top: 555px;
    display: flex; align-items: center; gap: 10px;
    font-family: "Roboto Condensed", sans-serif;
    font-size: 19px;
    color: var(--paper);
    letter-spacing: 0.3px;
  }
  .website {
    position: absolute;
    left: 905px; width: 200px; top: 557px;
    text-align: right;
    font-family: "Roboto Condensed", sans-serif;
    font-size: 19px;
    color: var(--paper);
  }
</style>
</head>
<body>
  <main class="backdrop">
    <svg class="backdrop-shapes" viewBox="0 0 1140 618" aria-hidden="true">
      <line x1="164" y1="332" x2="432" y2="332" stroke="#c9c9c9" stroke-width="1.2"/>
      <line x1="700" y1="332" x2="968" y2="332" stroke="#c9c9c9" stroke-width="1.2"/>
      <line x1="164" y1="427" x2="968" y2="426" stroke="#c9c9c9" stroke-width="1.2"/>
      <polygon points="728,603 1140,504 1140,618 760,618" fill="#dd137b"/>
      <polygon points="0,467 790,618 0,618" fill="#0b0b0c"/>
      <polygon points="0,545 98,618 0,618" fill="#e4549a"/>
    </svg>

    <div class="sparkle-field sparkle-field--top-left" role="img" aria-label="Scatter of pink and black sparkles and dots"></div>
    <div class="sparkle-field sparkle-field--bottom-right" role="img" aria-label="Small pink sparkles and dots"></div>
    <div class="staff-figures" role="img" aria-label="Faint line drawing of two healthcare workers"></div>

    <div class="client-mark"><span class="client-mark__dot"></span>QMRTE</div>

    <h1 class="event-title">
      <span class="event-title__org">QMRTE</span>
      <span class="event-title__name">Velvet Orchid Gala</span>
    </h1>

    <p class="sponsor-heading">THANK YOU <span class="sponsor-heading__small">to our</span> <span class="sponsor-heading__accent">SPONSORS</span></p>

    <ul class="sponsor-list">
      <li class="sponsor">Brindle Pathology</li>
      <li class="sponsor">Kestrel Radiology</li>
      <li class="sponsor">JNX Diagnostic Imaging</li>
      <li class="sponsor">Harwick Legal Group</li>
      <li class="sponsor"><span class="sponsor__square"></span>Dunmores</li>
    </ul>

    <p class="venue">
      <svg width="14" height="20" viewBox="0 0 14 20" aria-hidden="true">
        <path d="M7 0C3.1 0 0 3.1 0 7c0 5 7 13 7 13s7-8 7-13c0-3.9-3.1-7-7-7zm0 9.8A2.8 2.8 0 1 1 7 4.2a2.8 2.8 0 0 1 0 5.6z" fill="#ffffff"/>
      </svg>
      WEXLEY QUAY, SYDNEY
    </p>
    <p class="website">www.qmrte.org.au</p>
  </main>
</body>
</html>
```